Web Site Design for a Finance (lending) Company

We are opening a new subsidiary that focuses on lending money in the real estate industry. We need a web site designed to represent the business.

The business is lending money to real estate investors. A typical client/borrower will be looking to borrow money to buy a house, renovate it and then sell it at a profit, all within 12 months or less.

Company name is Brevand Finance. Our logo is attached.

Attached is a general outline for the web site. We're working on writing more text for each page but this should give you enough to get started with some ideas.

Competitor web site that I like a lot (as an example): https://quorvelfunding.com/. Many of the general items on this site match what we will need (description of loan programs, FAQ)

Target Market(s)

Real estate investors (generally individuals or small companies with just a few people) who are buying homes, renovating them and then selling them at a profit.

Industry/Entity Type

Finance

Coding

Coded - Design and coding required

Number of Pages Required

5+ page

Colors

Designer to choose colors to be used in the design.

Requirements
Must have
• Minimalist design. Clean lines without too much clutter. Some stock photography is ok but the photos should not be distracting. They should almost fade in to the background so that user can focus on the key information about what our company does instead. We are a finance company, not a design company, so the information about our products will be more interesting to site visitors than the art.
• Some minimalist examples from Snapboard:
• https://www.snapboard-example.com/explore/minimalist-web-design/
Nice to have
• If you search in seekly for "hard money lenders" you will find many examples of web sites from our competition. I have provided a link above to competitor web site that I like a lot.
• I have attached our logo in EPS format. Logo is green. Web site doesn't have to be green but it should be of a color that will work well with the logo.

```html
<!DOCTYPE html>
<html lang="en">
<head>
<meta charset="utf-8">
<title>Brevand Finance – Fix N Flip Loans</title>
<link href="https://fonts.googleapis.com/css2?family=Lato:wght@300;400;700;900&display=swap" rel="stylesheet">
<style>
  :root{
    --green:#00532f;
    --green-dark:#004426;
    --navy:#1d2b45;
    --grey-band:#efefef;
    --field:#f1f1f1;
    --text:#333;
    --muted:#8f8f8f;
    --white:#fff;
  }
  *{box-sizing:border-box;margin:0;padding:0}
  html,body{width:831px;height:1200px;overflow:hidden;background:var(--white)}
  body{position:relative;font-family:'Lato',sans-serif;color:var(--text)}
  .abs{position:absolute}

  /* header */
  .brand{left:110px;top:10px;display:flex;align-items:center;gap:8px}
  .brand-mark{width:18px;height:18px;background:var(--green)}
  .brand-name{font-size:15px;font-weight:700;color:var(--green);line-height:1.1}
  .call{left:552px;top:13px;display:flex;align-items:center;gap:6px}
  .call-icon{width:28px;height:28px;background:var(--green);border-radius:4px;display:flex;align-items:center;justify-content:center}
  .call-text{color:var(--green);font-weight:700;line-height:1}
  .call-text .big{font-size:19px;letter-spacing:.5px}
  .call-text .num{font-size:13px;color:#111}

  .nav{left:0;top:56px;width:831px;height:30px;background:var(--green)}
  .nav a{position:absolute;top:10px;color:var(--white);font-size:10px;font-weight:700;text-decoration:none;letter-spacing:.2px}
  .social-top{right:111px;top:6px;display:flex;gap:4px}
  .social-top span{width:17px;height:17px;background:var(--white);border-radius:3px;display:flex;align-items:center;justify-content:center}

  /* hero */
  .hero{left:0;top:86px;width:831px;height:149px;background:var(--grey-band)}
  .program-art{left:112px;top:112px;width:195px;height:90px;background:linear-gradient(135deg,#dfe7e2,#cfdcd4);border-radius:2px}
  .hero h1{left:323px;top:40px;font-size:18.5px;font-weight:400;color:#333}
  .hero p{left:325px;top:68px;width:390px;font-size:10.3px;font-weight:300;line-height:16.8px;color:var(--muted)}

  h2{position:absolute;font-size:18.5px;font-weight:400;color:#222}

  /* table */
  .rates{left:111px;top:306px;width:610px;border-collapse:collapse;table-layout:fixed;font-size:9.5px;border:1px solid var(--navy)}
  .rates th{background:var(--navy);color:var(--white);font-weight:700;height:26px;text-align:left;padding-left:6px;white-space:nowrap;font-size:9.6px}
  .rates td{height:25.6px;padding-left:6px;border-top:1px solid var(--navy);color:#333}
  .rates .c{text-align:center;padding-left:0}

  .copy{left:111px;width:608px;font-size:10.4px;font-weight:300;line-height:16.8px;color:var(--muted)}

  /* form */
  .field{position:absolute;width:247px;height:26px;background:var(--field);border:1px solid #555;font-size:9px;color:#666;padding:8px 6px 0}
  .field.select{padding-left:8px}
  .field.select::after{content:"";position:absolute;right:6px;top:12px;border:2px solid transparent;border-top:3px solid #333}
  .label{position:absolute;width:250px;font-size:10px;font-weight:700;color:#444;line-height:19px}
  .send{left:111px;top:889px;width:505px;height:25px;background:var(--green);color:var(--white);font-size:11px;font-weight:700;text-align:center;line-height:25px;border-radius:2px}

  /* footer */
  .footer{left:0;top:988px;width:831px;height:212px;background:var(--green)}
  .footer h3{position:absolute;top:37px;font-size:19px;font-weight:400;color:var(--white);letter-spacing:.5px}
  .footer ul{position:absolute;top:77px;list-style:none}
  .footer li{font-size:11.5px;font-weight:400;color:var(--white);height:22.8px}
  .signup{left:530px;top:76px;display:flex}
  .signup .email{width:134px;height:29px;background:var(--white);font-size:9px;color:#333;padding:10px 8px 0}
  .signup .btn{width:76px;height:29px;background:#0d1a14;color:var(--white);font-size:13px;font-weight:700;text-align:center;line-height:29px}
  .circles{left:528px;top:120px;display:flex;gap:5px}
  .circles span{width:24px;height:24px;border:1.5px solid var(--white);border-radius:50%;display:flex;align-items:center;justify-content:center}
  .rule{left:0;top:169px;width:831px;height:1px;background:rgba(255,255,255,.25)}
  .copyright{left:88px;top:186px;font-size:10px;color:var(--white)}
  .chat{left:519px;top:184px;width:222px;height:28px;background:var(--green-dark);color:var(--white);font-size:10px;padding:10px 8px 0;display:flex;justify-content:space-between}
  .chat .ctrl{display:flex;gap:6px}
  .chat .ctrl span{width:10px;height:10px;background:var(--white);border-radius:50%}
</style>
</head>
<body>

<header>
  <div class="abs brand"><span class="brand-mark"></span><span class="brand-name">Brevand Finance</span></div>
  <div class="abs call">
    <div class="call-icon">
      <svg width="16" height="16" viewBox="0 0 24 24"><path fill="#fff" d="M6.6 10.8a15 15 0 0 0 6.6 6.6l2.2-2.2a1 1 0 0 1 1-.25 11.4 11.4 0 0 0 3.6.57 1 1 0 0 1 1 1V20a1 1 0 0 1-1 1A17 17 0 0 1 3 4a1 1 0 0 1 1-1h3.5a1 1 0 0 1 1 1c0 1.25.2 2.45.57 3.57a1 1 0 0 1-.25 1z"/></svg>
    </div>
    <div class="call-text"><div class="big">CALL US</div><div class="num">555-014-LOAN (5626)</div></div>
  </div>
  <nav class="abs nav">
    <a style="left:110px">HOME</a>
    <a style="left:161px">ABOUT US</a>
    <a style="left:230px">LOAN</a>
    <a style="left:275px">RESOURCES</a>
    <a style="left:347px">CONTACT US</a>
    <div class="abs social-top">
      <span><svg width="11" height="11" viewBox="0 0 12 12"><path d="M1 2h10v6H5l-3 2.5V8H1z" fill="#00532f"/></svg></span>
      <span><svg width="11" height="11" viewBox="0 0 12 12"><circle cx="3" cy="6" r="1.6" fill="#00532f"/><circle cx="9" cy="2.5" r="1.6" fill="#00532f"/><circle cx="9" cy="9.5" r="1.6" fill="#00532f"/><path d="M3 6 9 2.5M3 6l6 3.5" stroke="#00532f" stroke-width="1.1"/></svg></span>
      <span><svg width="11" height="11" viewBox="0 0 12 12"><rect x="1" y="2.5" width="10" height="7" fill="none" stroke="#00532f" stroke-width="1.3"/><path d="M1 3l5 3.5L11 3" fill="none" stroke="#00532f" stroke-width="1.2"/></svg></span>
    </div>
  </nav>
</header>

<section class="abs hero">
  <h1 class="abs">Looking to Purchase and Rehab a Property?</h1>
  <p class="abs">Fixing and flipping homes is a great source of income, but it can be difficult to find the right funding. In order to renovate a home and flip it for a profit, you need sufficient capital.</p>
</section>
<div class="abs program-art" role="img" aria-label="Fix N Flip loan program logo"></div>

<h2 style="left:110px;top:263px">Fix N Flip Loan Overview</h2>
<table class="abs rates">
  <colgroup><col style="width:35px"><col style="width:90px"><col style="width:86px"><col style="width:73px"><col style="width:73px"><col style="width:72px"><col></colgroup>
  <tr><th>Level</th><th>Completed Flips</th><th>Origination Fee</th><th>Interest Rate</th><th>Loan-to-Cost</th><th>Loan-to-ARV</th><th>Interest on Undrawn Construction?</th></tr>
  <tr><td>1</td><td>0-1</td><td>3.5%</td><td>12%</td><td>90%</td><td>70%</td><td class="c">Yes</td></tr>
  <tr><td>2</td><td>2-4</td><td>3%</td><td>11%</td><td>90%</td><td>70%</td><td class="c">Yes</td></tr>
  <tr><td>3</td><td>5 - 14</td><td>2%</td><td>9.99%</td><td>90%</td><td>70%</td><td class="c">No</td></tr>
  <tr><td>4</td><td>15+</td><td>1.5%</td><td>7.99%</td><td>90%</td><td>70%</td><td class="c">No</td></tr>
</table>

<h2 style="left:111px;top:472px">Why choose Brevand</h2>
<p class="abs copy" style="top:499px">Lorem ipsum dolor sit amet, consectetuer adipiscing elit, sed diam nonummy nibh euismod tincidunt ut laoreet dolore magna aliquam erat volutpat. Ut wisi enim ad minim veniam, quis nostrud exerci tation ullamcorper suscipit lobortis nisl ut aliquip ex ea commodo consequat.</p>
<p class="abs copy" style="top:566px">Duis autem vel eum iriure dolor in hendrerit in vulputate velit esse molestie consequat, vel illum dolore eu feugiat nulla facilisis at vero eros et accumsan et iusto odio dignissim qui blandit praesent luptatum zzril delenit augue duis dolore te feugait nulla facilisi.</p>

<h2 style="left:111px;top:622px">Online Application</h2>
<div class="field" style="left:111px;top:664px">First Name</div>
<div class="field" style="left:370px;top:664px">Last Name</div>
<div class="field" style="left:111px;top:707px">Email Address</div>
<div class="field" style="left:370px;top:707px">Phone Number</div>
<div class="field" style="left:111px;top:752px">State</div>
<div class="field" style="left:370px;top:752px">City</div>
<div class="label" style="left:111px;top:793px">How did you hear about Quorvel Funding?</div>
<div class="label" style="left:370px;top:793px">How many Flips have you completed in the past 24 months?</div>
<div class="field select" style="left:111px;top:825px;height:27px">Broker</div>
<div class="field select" style="left:370px;top:839px;height:27px">0-1</div>
<div class="abs send">SEND</div>

<footer class="abs footer">
  <h3 style="left:86px">OUR INFO</h3>
  <h3 style="left:210px">BOOKING</h3>
  <h3 style="left:330px">ADDITIONAL LINKS</h3>
  <h3 style="left:528px">STAY CONNECTED</h3>
  <ul style="left:88px"><li>HOMEPAGE</li><li>ABOUT US</li><li>HIRING</li></ul>
  <ul style="left:211px"><li>BOOKING PAGE</li><li>BLOG</li></ul>
  <ul style="left:332px"><li>GIFT CARD</li><li>HELP</li><li>WE'RE GREEN</li></ul>
  <div class="abs signup"><div class="email">EMAIL</div><div class="btn">SIGN UP</div></div>
  <div class="abs circles">
    <span><svg width="11" height="11" viewBox="0 0 12 12"><path d="M1 2h10v6H5l-3 2.5V8H1z" fill="#fff"/></svg></span>
    <span><svg width="11" height="11" viewBox="0 0 12 12"><circle cx="3" cy="6" r="1.6" fill="#fff"/><circle cx="9" cy="2.5" r="1.6" fill="#fff"/><circle cx="9" cy="9.5" r="1.6" fill="#fff"/><path d="M3 6 9 2.5M3 6l6 3.5" stroke="#fff" stroke-width="1.1"/></svg></span>
    <span><svg width="11" height="11" viewBox="0 0 12 12"><rect x="1" y="2.5" width="10" height="7" fill="none" stroke="#fff" stroke-width="1.3"/><path d="M1 3l5 3.5L11 3" fill="none" stroke="#fff" stroke-width="1.2"/></svg></span>
    <span><svg width="11" height="11" viewBox="0 0 12 12"><path d="M6 11S2 6.8 2 4.5a4 4 0 0 1 8 0C10 6.8 6 11 6 11z" fill="#fff"/><circle cx="6" cy="4.5" r="1.4" fill="#00532f"/></svg></span>
  </div>
  <div class="abs rule"></div>
  <div class="abs copyright">Copyright Brevand @2017</div>
  <div class="abs chat">Live Chat<div class="ctrl"><span></span><span></span></div></div>
</footer>

</body>
</html>
```